Personal Training Studio Checkin App (or URL based)

I would like a simple web based app built for our  business. We have a training studio with a simple business model. All our clients buy sessions in packages either 4, 8, or 12 at a time. We want something that a trainer can pull up and Check in a client. This will record the date and time the client was checked in, by what trainer, and what type of session. This system will keep track of the following:
Whenever a Client Checks in so it will ‘tick off’ a session on their package (ie- they have gone from 11 sessions left to 10 sessions left)
Track what sessions a particular trainer does so we can pay them at the end of the week and look at who they trained, what type of session and how many
Look at client activity: Every time they check in, Recharge their package, any activity related to the client, even if it was admin – like deleting a session that was mistakenly recorded.
This will keep a database of clients added and all their activity
The pdf I have included lays out how I think it would work and the features I want
I would like this to run off an tablora that we have at our front check in counter. It can be an app or a URL that use.
***THIS PROJECT IS NOT SO MUCH ABOUT DESIGN BUT ABOUT FUNCTIONALITY OF THE APPLICATION. IT MUST HAVE THE FEATURES I HAVE ASKED FOR THAT WORK TOGETHER. I AM WILLING TO PAY A LITTLE MORE AS A BONUS IF YOU CAN ACCOMPLISH THIS. ALSO IF I FIN THE RIGHT PERSON THAT CAN DO THIS I WILL MAKE IT A GUARNTEED PROJECT.

- Functionality and Track and record all the info we need

```html
<!DOCTYPE html>
<html lang="en">
<head>
<meta charset="utf-8">
<title>Ironline Studio – Activity Log</title>
<link href="https://fonts.googleapis.com/css2?family=Nunito+Sans:wght@400;600;700;800&display=swap" rel="stylesheet">
<style>
  :root {
    --page-bg: #dcdcdc;
    --card-bg: #ffffff;
    --nav-bg: #fafaf9;
    --halo: rgba(0, 0, 0, 0.03);
    --ink: #2a2d34;
    --ink-soft: #3d424b;
    --muted: #6f7682;
    --brand-grey: #5b5b5d;
    --brand-orange: #ff4a0a;
    --accent: #6c7ce4;
    --accent-start: #6c7fe6;
    --accent-end: #7a4fb0;
    --line: #e4e8ee;
    --field-line: #d9dee6;
    --scroll-track: #f0f0f0;
    --scroll-thumb: #c4c4c4;
  }
  * { box-sizing: border-box; margin: 0; padding: 0; }
  html, body {
    width: 1200px; height: 689px; overflow: hidden;
    background: var(--page-bg);
    font-family: "Nunito Sans", "Segoe UI", sans-serif;
    color: var(--ink);
  }
  .app { position: relative; width: 1200px; height: 689px; }

  .card {
    position: absolute; left: 235px; width: 731px;
    background: var(--card-bg);
    border-radius: 13px;
    box-shadow: 0 0 0 10px var(--halo), 0 2px 6px rgba(0,0,0,0.05);
  }

  /* Header */
  .header { top: 13px; height: 189px; text-align: center; }
  .brand {
    position: absolute; top: 62px; left: 0; right: 0;
    display: flex; align-items: center; justify-content: center; gap: 12px;
  }
  .brand-mark { width: 26px; height: 26px; background: var(--brand-orange); }
  .brand-name {
    font-size: 44px; font-weight: 800; letter-spacing: 1px;
    color: var(--brand-grey); line-height: 1;
  }
  .tagline {
    position: absolute; top: 155px; left: 0; right: 0;
    font-size: 11.5px; color: var(--muted);
  }

  /* Navigation */
  .nav {
    top: 221px; height: 43px; background: var(--nav-bg);
    display: flex; align-items: center; padding: 0 6px;
    border-radius: 9px;
  }
  .nav-tab {
    flex: 1; height: 31px; display: flex; align-items: center; justify-content: center;
    font-size: 11px; font-weight: 700; color: var(--ink-soft);
    border-radius: 6px;
  }
  .nav-tab.is-active {
    color: #fff;
    background: linear-gradient(90deg, var(--accent-start), var(--accent-end));
    box-shadow: 0 3px 8px rgba(108, 124, 228, 0.35);
  }

  /* Activity panel */
  .panel { top: 283px; height: 375px; padding: 0 19px; }
  .panel-title {
    position: absolute; top: 21px; left: 19px;
    font-size: 15.5px; font-weight: 800; color: var(--ink);
  }
  .filter-label {
    position: absolute; top: 40px; left: 19px;
    font-size: 9.5px; font-weight: 600; color: var(--ink-soft);
  }
  .filter-select {
    position: absolute; top: 58px; left: 18px; width: 694px; height: 33px;
    border: 1.5px solid var(--field-line); border-radius: 7px;
    display: flex; align-items: center; justify-content: space-between;
    padding: 0 8px 0 10px; font-size: 10px; color: #111;
  }
  .filter-select svg { width: 8px; height: 8px; }

  .log {
    position: absolute; top: 104px; left: 18px; width: 694px; height: 251px;
    border: 1.5px solid var(--line); border-radius: 5px; overflow: hidden;
  }
  .log-list { position: absolute; top: 0; left: 10px; right: 22px; }
  .log-item {
    height: 71px; padding: 20px 0 0 8px;
    border-bottom: 1px solid var(--line);
  }
  .log-item:first-child { height: 74px; padding-top: 22px; }
  .log-type { font-size: 10px; font-weight: 600; color: var(--accent); line-height: 1; }
  .log-text { font-size: 9.6px; color: var(--ink-soft); margin-top: 7px; line-height: 1; }
  .log-time { font-size: 8.2px; color: var(--muted); margin-top: 7px; line-height: 1; }

  .scrollbar {
    position: absolute; top: 0; right: 0; width: 11px; height: 100%;
    background: var(--scroll-track);
  }
  .scroll-thumb {
    position: absolute; top: 11px; left: 1px; width: 9px; height: 117px;
    background: var(--scroll-thumb);
  }
  .scroll-arrow { position: absolute; left: 2px; width: 7px; height: 7px; }
  .scroll-arrow.up { top: 2px; }
  .scroll-arrow.down { bottom: 2px; }
</style>
</head>
<body>
<div class="app">
  <header class="card header">
    <div class="brand">
      <span class="brand-mark"></span>
      <span class="brand-name">IRONLINE STUDIO</span>
    </div>
    <p class="tagline">Check-in clients, track sessions, and manage your training business</p>
  </header>

  <nav class="card nav">
    <div class="nav-tab">Check-in</div>
    <div class="nav-tab">Clients</div>
    <div class="nav-tab">Trainers</div>
    <div class="nav-tab is-active">Activity Log</div>
  </nav>

  <section class="card panel">
    <h2 class="panel-title">Activity Log</h2>
    <div class="filter-label">Filter by Type:</div>
    <div class="filter-select">
      <span>All Activities</span>
      <svg viewBox="0 0 10 10"><path d="M2 3.5 L5 6.5 L8 3.5" fill="none" stroke="#222" stroke-width="1.6"/></svg>
    </div>

    <div class="log">
      <div class="log-list">
        <div class="log-item">
          <div class="log-type">Check-in</div>
          <div class="log-text">Testing checked in for Partner Session (Only 1 Party Showed) by Sam Reyes</div>
          <div class="log-time">7/5/2025, 11:52:09 PM</div>
        </div>
        <div class="log-item">
          <div class="log-type">Package Recharge</div>
          <div class="log-text">Dario recharged with 4 sessions</div>
          <div class="log-time">7/5/2025, 11:51:13 PM</div>
        </div>
        <div class="log-item">
          <div class="log-type">New Trainer</div>
          <div class="log-text">New trainer added: Nora Whitfield</div>
          <div class="log-time">7/5/2025, 11:50:52 PM</div>
        </div>
        <div class="log-item">
          <div class="log-type">New Client</div>
        </div>
      </div>
      <div class="scrollbar">
        <svg class="scroll-arrow up" viewBox="0 0 10 10"><path d="M2 6.5 L5 3.5 L8 6.5" fill="none" stroke="#555" stroke-width="1.5"/></svg>
        <div class="scroll-thumb"></div>
        <svg class="scroll-arrow down" viewBox="0 0 10 10"><path d="M2 3.5 L5 6.5 L8 3.5" fill="none" stroke="#555" stroke-width="1.5"/></svg>
      </div>
    </div>
  </section>
</div>
</body>
</html>
```